CD Cover Design Project

Although I posted a picture as a possible idea, an idea from scratch is mostly what I am looking for. Definitely listen to the song before making the design. The link is posted right here in the project overview.
I need a CD cover for my latest single. This artwork will go up on Melodeck, brimora, etc with the song. Please listen to the song and then creat the artwork. Here is a link to the song:
http://tunevaultmusic.net/doriancolewhitfield/where-the-rivers-bend
The design needs my name, Dorian Cole Whitfield and it needs the song title, Where the Rivers Bend.
It needs to be a perfect square.
1600 by 1600
Resolution 300 DPI
Contact me at dorian@dorian-cole.net or (503) 482-3091

```html
<!DOCTYPE html>
<html lang="en">
<head>
<meta charset="utf-8">
<title>Dorian Cole Whitfield – Where the Rivers Bend</title>
<link rel="stylesheet" href="https://fonts.googleapis.com/css2?family=Archivo+Black&display=swap">
<style>
  :root {
    --frame: #f2f8cc;
    --frame-edge: #dcebb0;
    --field-light: #86ab80;
    --field: #6c9467;
    --field-dark: #557c52;
    --ink-pale: #eff8dc;
    --ink-shadow: #3a2a22;
    --ink-dark: #2c2a26;
    --band-light: #ffffff;
    --band-mid: #e6f6d2;
    --band-edge: #c8e8b4;
  }
  html, body {
    margin: 0;
    padding: 0;
    width: 1200px;
    height: 1200px;
    overflow: hidden;
    background: var(--frame);
  }
  .cover {
    position: relative;
    width: 1200px;
    height: 1200px;
    background:
      radial-gradient(circle at 10% 90%, var(--frame-edge) 0%, transparent 40%),
      radial-gradient(circle at 95% 8%, var(--frame-edge) 0%, transparent 35%),
      var(--frame);
    font-family: "Archivo Black", "Arial Black", sans-serif;
  }
  .cover__field {
    position: absolute;
    left: 27px;
    top: 27px;
    width: 1146px;
    height: 1146px;
    background:
      radial-gradient(ellipse at 50% 45%, var(--field-light) 0%, var(--field) 55%, var(--field-dark) 100%);
    box-shadow: inset 0 0 60px rgba(40, 70, 40, 0.45);
    overflow: hidden;
  }
  .cover__bands {
    position: absolute;
    inset: 0;
    width: 100%;
    height: 100%;
  }
  .artist, .title {
    position: absolute;
    left: 0;
    width: 100%;
    margin: 0;
    text-align: center;
    color: var(--ink-pale);
    text-shadow: 4px 5px 0 var(--ink-shadow);
    font-weight: 400;
    line-height: 1;
  }
  .artist {
    top: 195px;
    font-size: 92px;
    letter-spacing: 1px;
  }
  .artist__line {
    display: block;
    margin-bottom: 32px;
  }
  .title {
    top: 860px;
    font-size: 68px;
    letter-spacing: 0;
  }
  .title__accent {
    color: var(--ink-dark);
    text-shadow: 2px 3px 0 rgba(240, 248, 220, 0.6);
  }
</style>
</head>
<body>
  <div class="cover">
    <div class="cover__field">
      <svg class="cover__bands" viewBox="0 0 764 764" preserveAspectRatio="none" aria-hidden="true">
        <defs>
          <linearGradient id="band-glow" x1="0" y1="0" x2="1" y2="0">
            <stop offset="0" stop-color="var(--band-edge)"/>
            <stop offset="0.55" stop-color="var(--band-light)"/>
            <stop offset="1" stop-color="var(--band-edge)"/>
          </linearGradient>
        </defs>
        <polygon class="band band--short" points="0,430 270,349 270,386 0,468" fill="url(#band-glow)" opacity="0.9"/>
        <polygon class="band band--long" points="0,500 764,270 764,310 0,540" fill="url(#band-glow)" opacity="0.95"/>
        <polygon class="band band--right" points="424,452 764,350 764,386 424,489" fill="url(#band-glow)" opacity="0.9"/>
      </svg>
      <h1 class="artist">
        <span class="artist__line">Dorian Cole</span>
        <span class="artist__line">Whitfield</span>
      </h1>
      <h2 class="title">Where <span class="title__accent">the</span> Rivers Bend</h2>
    </div>
  </div>
</body>
</html>
```